Ironbark & Vale Construction and Developments business cards

A business card with watermark background (construction work)

Home improvement projects
House renovations
Bathroom and kitchen renovations
House extensions
New builds and granny flats

Director Tomas Verhoeven
(Phone number)
tomas@ivkbuilds.com.au
(Instagram logo) ivk_builds

```html
<!DOCTYPE html>
<html lang="en">
<head>
<meta charset="utf-8">
<title>Ironbark &amp; Vale – Business Cards</title>
<link href="https://fonts.googleapis.com/css2?family=Source+Sans+3:wght@300;400;600;700&display=swap" rel="stylesheet">
<style>
  :root {
    --bg: #000000;
    --brand-blue: #2f74bf;
    --band-blue: #3a7cc4;
    --band-grey: #c4c4c4;
    --paper: #ffffff;
    --ink: #2a2a2a;
    --slate: #4f4f4f;
    --divider: #8a8a8a;
    --white: #ffffff;
  }
  * { box-sizing: border-box; margin: 0; padding: 0; }
  html, body { width: 825px; height: 1200px; overflow: hidden; }
  body {
    background: var(--bg);
    font-family: "Source Sans 3", "Source Sans Pro", sans-serif;
    position: relative;
  }
  .card {
    position: absolute;
    left: 62px;
    width: 700px;
    height: 400px;
    border-radius: 10px;
    overflow: hidden;
  }
  .card-front { top: 170px; background: var(--paper); }
  .card-back { top: 630px; background: var(--slate); }

  .front-band { position: absolute; left: 0; top: 0; width: 700px; height: 160px; }
  .band-watermark {
    position: absolute; left: 420px; top: 0; width: 260px; height: 90px;
    background: radial-gradient(ellipse at center, rgba(110,160,215,0.45) 0%, rgba(110,160,215,0) 70%);
  }

  .holder { position: absolute; left: 24px; top: 138px; }
  .holder-name { color: var(--brand-blue); font-size: 28px; font-weight: 400; line-height: 1.1; }
  .holder-role { color: var(--ink); font-size: 20px; font-weight: 400; line-height: 1.1; }

  .contact-list { position: absolute; left: 24px; top: 232px; list-style: none; }
  .contact-list li {
    display: flex; align-items: center; gap: 10px;
    color: var(--ink); font-size: 18px; line-height: 30px;
  }
  .contact-icon { width: 14px; height: 14px; flex: none; }

  .services {
    position: absolute; left: 24px; right: 24px; top: 348px;
    display: flex; justify-content: space-between;
    color: var(--brand-blue); font-size: 19px;
  }
  .services .divider { color: var(--divider); }

  .brand-mark {
    position: absolute; display: flex; align-items: center; gap: 8px;
    font-weight: 600; white-space: nowrap;
  }
  .brand-mark .mark-square { width: 14px; height: 14px; flex: none; }
  .card-front .brand-mark { right: 26px; top: 270px; color: var(--brand-blue); font-size: 21px; }
  .card-front .mark-square { background: var(--brand-blue); }
  .card-back .brand-mark { right: 26px; top: 330px; color: var(--white); font-size: 22px; }
  .card-back .mark-square { background: var(--white); }

  .back-watermark {
    position: absolute; left: 0; top: 60px; width: 700px; height: 340px;
    background: radial-gradient(ellipse at 55% 50%, rgba(110,110,110,0.6) 0%, rgba(110,110,110,0) 65%);
  }
  .company { position: absolute; left: 26px; top: 26px; color: var(--white); }
  .company-name { font-size: 34px; font-weight: 700; line-height: 1; letter-spacing: 0.3px; }
  .company-line { font-size: 17px; font-weight: 300; letter-spacing: 0.2px; margin-top: 4px; }
  .website { position: absolute; left: 26px; top: 358px; color: var(--white); font-size: 18px; }
  .website .domain { color: var(--brand-blue); }
</style>
</head>
<body>

<section class="card card-front">
  <svg class="front-band" viewBox="0 0 700 160" aria-hidden="true">
    <path d="M0 12 C150 10 300 30 420 95 C500 140 590 130 700 92 V0 H0 Z" fill="var(--band-grey)"/>
    <path d="M0 0 H700 V80 C590 118 510 125 430 85 C310 22 150 6 0 22 Z" fill="var(--band-blue)"/>
  </svg>
  <div class="band-watermark" role="img" aria-label="Faint house rooftops watermark in the blue band"></div>

  <div class="holder">
    <p class="holder-name">Tomas Verhoeven</p>
    <p class="holder-role">Director</p>
  </div>

  <ul class="contact-list">
    <li>
      <svg class="contact-icon" viewBox="0 0 16 16" aria-hidden="true"><path d="M3 1 L6 1 L7 5 L5 6.5 C6 9 7.5 10.5 9.5 11 L11 9 L15 10 L15 13 C15 14 14 15 13 15 C6.5 14.5 1.5 9.5 1 3 C1 2 2 1 3 1 Z" fill="var(--brand-blue)"/></svg>
      <span>000-555-7821</span>
    </li>
    <li>
      <svg class="contact-icon" viewBox="0 0 16 16" aria-hidden="true"><path d="M1 2 L15 8 L1 14 L4 8 Z" fill="var(--brand-blue)"/></svg>
      <span>tomas@ivkbuilds.com.au</span>
    </li>
    <li>
      <svg class="contact-icon" viewBox="0 0 16 16" aria-hidden="true"><rect x="2" y="2" width="12" height="12" fill="var(--brand-blue)"/></svg>
      <span>ivk_builds</span>
    </li>
  </ul>

  <div class="brand-mark"><span class="mark-square"></span><span>Ironbark &amp; Vale</span></div>

  <p class="services">
    <span>Improvement</span><span class="divider">|</span>
    <span>Renovations</span><span class="divider">|</span>
    <span>Extensions</span><span class="divider">|</span>
    <span>New Builds</span><span class="divider">|</span>
    <span>Granny Flats</span>
  </p>
</section>

<section class="card card-back">
  <div class="back-watermark" role="img" aria-label="Faint large watermark with construction and house motif"></div>
  <div class="company">
    <p class="company-name">IRONBARK &amp; VALE</p>
    <p class="company-line">CONSTRUCTION AND DEVELOPMENTS</p>
  </div>
  <div class="brand-mark"><span class="mark-square"></span><span>Ironbark &amp; Vale</span></div>
  <p class="website">www.<span class="domain">ivkbuilds</span>.com.au</p>
</section>

</body>
</html>
```